Broschüre KTR Festival
Zielgruppe
Wir sind ein Verband, der Ensembles der Amateurmusik (Blasorchester, Chöre, Akkordeonensembles ....) vertritt. Unsere Zielgruppe sind Menschen, die in ihrer Freizeit musizieren ebenso, wie Menschen die gerne Konzerte besuchen.
Die Broschüre ist ein Programmheft für ein eintägiges Festival mit mehreren Open-Air Bühnen.
Aufgabenstellung
Die Broschüre sollte DIN lang Format sein, damit sie gut in die Westentasche passt. Zentraler Bestandteil neben den Textseiten sind die Termintabellen, die die Auftritte auf den Bühnen abbilden.

```html
<!DOCTYPE html>
<html lang="de">
<head>
<meta charset="utf-8">
<title>KTR Festival – Programmheft</title>
<link href="https://fonts.googleapis.com/css2?family=Open+Sans:wght@400;600;700;800&family=Oswald:wght@300;500&display=swap" rel="stylesheet">
<style>
  :root {
    --teal: #25b5a0;
    --teal-dark: #1d9886;
    --tan: #9b8a78;
    --paper-grey: #ecebe9;
    --white: #ffffff;
    --ink: #4a4a4a;
    --stage: #d6d6d6;
    --red: #e2363f;
    --yellow: #f2c318;
    --blue: #3457a8;
  }
  * { box-sizing: border-box; margin: 0; padding: 0; }
  html, body { width: 1200px; height: 750px; overflow: hidden; }
  body {
    background: var(--stage);
    font-family: "Open Sans", Arial, sans-serif;
    position: relative;
  }
  .brochure {
    position: absolute;
    left: 40px; top: 65px;
    width: 1120px; height: 620px;
    display: flex;
    box-shadow: 0 10px 30px rgba(0,0,0,.18);
  }
  .panel {
    position: relative;
    width: 280px; height: 620px;
    overflow: hidden;
  }
  .panel::before, .panel::after {
    content: "";
    position: absolute; left: 0; right: 0; height: 7px;
    background: linear-gradient(to bottom,
      var(--red) 0 2px, var(--white) 2px 3px,
      var(--yellow) 3px 4px, var(--white) 4px 5px,
      var(--blue) 5px 7px);
    z-index: 3;
  }
  .panel::before { top: 10px; }
  .panel::after { bottom: 10px; transform: scaleY(-1); }

  /* Panel 1 – Festival text */
  .panel--intro { background: var(--paper-grey); padding: 40px 26px; }
  .section-title {
    font-family: "Oswald", "Arial Narrow", sans-serif;
    font-size: 19px; letter-spacing: .5px; text-align: right;
    margin-bottom: 8px;
  }
  .section-title .light { color: var(--teal); font-weight: 300; }
  .section-title .bold { color: var(--tan); font-weight: 500; }
  .body-copy {
    font-size: 9.6px; line-height: 1.55; color: var(--ink);
    text-align: justify; margin-bottom: 12px;
  }
  .lead { text-align: right; }
  .intro-brand { margin: 18px 0 20px; color: var(--teal); }
  .brand-name { font-weight: 800; font-size: 26px; line-height: 1.05; }
  .brand-date { font-weight: 700; font-size: 16px; line-height: 1.2; }

  /* Panel 2 – Partners */
  .panel--partners { background: var(--white); padding: 40px 24px; }
  .panel--partners .section-title { text-align: left; }
  .partner-list {
    display: grid; grid-template-columns: 1fr 1fr;
    gap: 10px 14px; margin-top: 12px;
  }
  .partner { font-weight: 700; font-size: 13px; color: #222; }
  .partner--blue { color: var(--blue); }
  .partner-deco {
    position: absolute; left: 40px; top: 230px;
    color: var(--teal); font-weight: 800;
    font-size: 118px; line-height: .9;
  }

  /* Panel 3 – Info */
  .panel--info { background: var(--teal); color: var(--white); }
  .orchestra-photo {
    position: absolute; inset: 0 0 150px 0;
    background: linear-gradient(160deg, #35bca8 0%, #2aa893 45%, #1f9a86 100%);
  }
  .info-block {
    position: absolute; left: 22px; right: 16px; bottom: 48px;
    display: flex; gap: 14px; align-items: flex-start;
  }
  .info-brand .brand-name { font-size: 17px; }
  .info-brand .brand-date { font-size: 11px; }
  .contact { font-size: 9.5px; line-height: 1.6; }
  .contact-title { font-weight: 700; font-size: 11px; margin-bottom: 4px; }
  .contact-line { display: flex; align-items: center; gap: 5px; }
  .contact-line svg { width: 9px; height: 9px; flex: none; }

  /* Panel 4 – Cover */
  .panel--cover { background: var(--teal); color: var(--white); }
  .cover-art {
    position: absolute; left: 0; right: 0; top: 18px; height: 290px;
    background: radial-gradient(ellipse at 50% 50%, #8e8176 0%, #a39486 40%, #cfc6bd 75%, #f3f1ee 100%);
  }
  .cover-brand {
    position: absolute; left: 80px; top: 140px; z-index: 2;
  }
  .cover-brand .brand-name { font-size: 30px; }
  .cover-brand .brand-date { font-size: 18px; }
  .slogan {
    position: absolute; left: 0; right: 0; top: 370px;
    text-align: center; font-weight: 800; font-size: 28px;
    line-height: 1.1; letter-spacing: .5px;
  }
</style>
</head>
<body>
<main class="brochure">

  <section class="panel panel--intro">
    <h2 class="section-title"><span class="light">THE </span><span class="bold">FESTIVAL</span></h2>
    <p class="body-copy lead">Das Festival bringt Chöre, Blasorchester und Akkordeonensembles aus dem ganzen Land an einem Tag zusammen. Auf mehreren Bühnen unter freiem Himmel zeigen Amateurmusiker, was sie in ihrer Freizeit gemeinsam erarbeitet haben.</p>
    <div class="intro-brand">
      <div class="brand-name">KTR Festival</div>
      <div class="brand-date">11.07.2020<br>Überlingen</div>
    </div>
    <p class="body-copy">Besucher können frei zwischen den Bühnen wechseln und erleben so Musik aller Stilrichtungen. Die Termintabellen in diesem Heft zeigen, wann welches Ensemble auftritt.</p>
    <p class="body-copy">Zwischen den Konzerten laden Stände am Seeufer zum Verweilen ein. Der Eintritt zu allen Bühnen ist frei, Spenden unterstützen die Arbeit der Vereine.</p>
    <p class="body-copy">Wir freuen uns auf einen Tag voller Klang, Begegnung und Freude am gemeinsamen Musizieren.</p>
  </section>

  <section class="panel panel--partners">
    <h2 class="section-title"><span class="light">MAIN </span><span class="bold">PARTNERS</span></h2>
    <div class="partner-list">
      <span class="partner">Nordkauf</span>
      <span class="partner"></span>
      <span class="partner">Pastaria</span>
      <span class="partner"></span>
      <span class="partner">Geländer</span>
      <span class="partner partner--blue">Meerlinie</span>
      <span class="partner partner--blue">Voltwerk</span>
    </div>
    <div class="partner-deco">KTR</div>
  </section>

  <section class="panel panel--info">
    <div class="orchestra-photo" role="img" aria-label="Foto eines Orchesters bei einem Open-Air-Konzert, teal eingefärbt"></div>
    <div class="info-block">
      <div class="info-brand">
        <div class="brand-name">KTR Festival</div>
        <div class="brand-date">11.07.2020<br>Überlingen</div>
      </div>
      <div class="contact">
        <div class="contact-title">Info and Tickets</div>
        <div class="contact-line">
          <svg viewBox="0 0 10 10"><path d="M2 1h2l1 2.5-1.2.8a5 5 0 0 0 2 2l.8-1.2L9 6v2a1 1 0 0 1-1 1A7 7 0 0 1 1 2a1 1 0 0 1 1-1z" fill="currentColor"/></svg>
          +49 00 12 34 56 789
        </div>
        <div class="contact-line">tickets@ktr-festival.de</div>
        <div class="contact-line">www.ktr-festival.de</div>
      </div>
    </div>
  </section>

  <section class="panel panel--cover">
    <div class="cover-art" role="img" aria-label="Rauchwolke mit schwebenden Musikinstrumenten: Harfe, Trompete, Flügel und Violinen"></div>
    <div class="cover-brand">
      <div class="brand-name">KTR<br>Festival</div>
      <div class="brand-date">11.07.2020<br>Überlingen</div>
    </div>
    <p class="slogan">NATÜRLICH<br>MUSIK!</p>
  </section>

</main>
</body>
</html>
```